Product Factsheet

We are seeking a talented graphic designer to prepare a technical and product factsheet based a range of products which are installed offshore and subsea.

A third-party has generated some rendered images of each of our products together with a master-scene showing each installed (around 13 - 15 products).

Our intention is to create a single page factsheet with call-outs on each product providing some basic information and data.

Our company logo shall require to be incorporated however this shall be provided at a later date due to confidentiality.

Target Market(s)

Global audience with an understanding of our product with an ability to understand technical and complex products

Industry/Entity Type

Oil And Gas

Font styles to use
Serif

Requirements
Must have
• Flexibility - in case we need to increase the product portfolio at a later date
Should not have
• The design of the flyer should no compromise the design of the subsea render

```html
<!DOCTYPE html>
<html lang="en">
<head>
<meta charset="utf-8">
<title>Product Factsheet</title>
<link rel="stylesheet" href="https://fonts.googleapis.com/css2?family=Montserrat:wght@400;600;800&display=swap">
<style>
  :root {
    --backdrop: #333132;
    --paper: #ffffff;
    --brand-blue: #176a8f;
    --ink: #4a4a4a;
    --heading-ink: #3c3c3c;
    --band-light: #b8d6e0;
    --band-dark: #176a8f;
  }
  * { box-sizing: border-box; margin: 0; padding: 0; }
  html, body { width: 1200px; height: 1200px; overflow: hidden; }
  body {
    background: var(--backdrop);
    font-family: "Montserrat", Arial, sans-serif;
    position: relative;
  }
  .factsheet {
    position: absolute;
    left: 210px; top: 48px;
    width: 780px; height: 1104px;
    background: var(--paper);
    overflow: hidden;
  }
  .hero {
    position: absolute; left: 0; top: 0;
    width: 780px; height: 562px;
    display: block;
  }
  .title-block {
    position: absolute; left: 47px; top: 558px;
  }
  .product-name {
    font-weight: 800;
    font-size: 45px;
    line-height: 1;
    color: var(--brand-blue);
    letter-spacing: 0.2px;
  }
  .product-type {
    font-weight: 400;
    font-size: 29px;
    line-height: 1.2;
    color: var(--heading-ink);
    margin-top: 2px;
  }
  .intro {
    position: absolute; left: 47px; top: 686px;
    width: 345px;
    font-size: 14.2px;
    line-height: 18.9px;
    color: var(--ink);
  }
  .features {
    position: absolute; left: 400px; top: 686px;
    width: 340px;
    list-style: none;
    font-weight: 600;
    font-size: 14.2px;
    line-height: 18.9px;
    color: var(--brand-blue);
  }
  .features li { position: relative; padding-left: 10px; }
  .features li::before {
    content: "•"; position: absolute; left: 0; top: 0;
  }
  .detail-render {
    position: absolute; left: 398px; top: 822px;
    width: 335px; height: 202px;
    background: linear-gradient(160deg, #8f7c62 0%, #a88d6c 45%, #8c7358 100%);
  }
  .footer-band {
    position: absolute; left: 0; bottom: 0;
    width: 780px; height: 48px;
    background: linear-gradient(90deg, var(--band-light) 0%, #5f9db5 55%, var(--band-dark) 100%);
  }
</style>
</head>
<body>
  <main class="factsheet">
    <svg class="hero" viewBox="0 0 780 562" role="img" aria-label="Rendered offshore scene: platform and support vessel on the sea surface above installed subsea products on the seabed">
      <defs>
        <linearGradient id="scene-tones" x1="0" y1="0" x2="0" y2="1">
          <stop offset="0" stop-color="#cfe3ee"/>
          <stop offset="0.18" stop-color="#e9eef1"/>
          <stop offset="0.3" stop-color="#6f9bb0"/>
          <stop offset="0.52" stop-color="#3f7791"/>
          <stop offset="0.56" stop-color="#1d4a5c"/>
          <stop offset="0.72" stop-color="#5d6a63"/>
          <stop offset="1" stop-color="#8e7558"/>
        </linearGradient>
      </defs>
      <rect width="780" height="562" fill="url(#scene-tones)"/>
      <polygon points="0,526 733,526 780,560 780,562 0,562" fill="#ffffff"/>
      <polyline points="0,526 733,526 780,560" fill="none" stroke="#176a8f" stroke-width="3"/>
    </svg>

    <header class="title-block">
      <h1 class="product-name">PRODUCT NAME</h1>
      <p class="product-type">Product type</p>
    </header>

    <div class="intro">
      Aque nonet optinct oritatest, occus re volest, id<br>
      esed maxime nume dolupta ectota ipsus.<br>
      Ga. Iquaecum quam sa qui tem. Natibus, occus.<br>
      Mus as derspiet, sita dolupistrum rehentio dolo-<br>
      rum et facepratque cum natem iur, omnis exero<br>
      intur sum rectur? Antem earumquia ium qui<br>
      des perchil idem et aut vero tet aspis a inusam<br>
      alis nobit pro invel moluptasped et et omnimpe<br>
      licatib eaquam hitaspe pa quidebitatet harchil<br>
      moluptate volorporro cusant re perore, tor seque<br>
      ne volore nus.<br>
      It, odiasimagnis il expe non cus accatque vellab-<br>
      ora venimolessi cum el magnatque eosanis<br>
      eruptiundam, simi, sint pe velest omnienist, offi-<br>
      cipid esseri il escium volor solupta nulpa dolor a<br>
      nobis prem. Hent.<br>
      Itae qui dest, nulpa corum harumet alitasp ere-<br>
      pro evelendest, con comnihi ciatur
    </div>

    <ul class="features">
      <li>Ximagnihitat et molupta simus.</li>
      <li>Onsequaesti re rest, quo issitia nonsed utem et alitae dolorum, si ut as dolorae ent isquos nus etur sequat.</li>
      <li>Nissequo que sedis sant eossi cus, quo odit a</li>
    </ul>

    <div class="detail-render" role="img" aria-label="Close-up render of a subsea product installed on the seabed with connecting lines"></div>

    <div class="footer-band"></div>
  </main>
</body>
</html>
```